Business Card Design Project

Hello Designers, hope you are all aiming enjoy the weekend
I have the Business Logo (uploaded), you can alter the color which ever way you think would work,
Im looking for a simple yet striking feel, something which will stay memorable (I have uploaded 3 examples for you to flick through)
Information on the card, will just be the bare minimum,
Double Sided
Info being
i.e.
Name
Number
Website
ABN
Tobin Wexmoor
+468213579 (singapore)
+315792846 (Australia)
+729384615 (America)
www.lomevu-linkup.example
ABN 86420913
Enjoy,
Tobin
Industry/Entity Type
Business
Look and feel
Each slider illustrates characteristics of the customer's brand and the style your logo design should communicate.

```html
<!DOCTYPE html>
<html lang="en">
<head>
<meta charset="utf-8">
<title>Lomevu Linkup – Business Card</title>
<link rel="stylesheet" href="https://fonts.googleapis.com/css2?family=Comfortaa:wght@400;700&family=Delius&display=swap">
<style>
  :root {
    --backdrop: #2b2725;
    --card-pink: #f8c8d1;
    --card-pink-light: #fde3e8;
    --card-pink-deep: #f2aebb;
    --brand-crimson: #c61f3f;
    --text-grey: #6a6a6a;
    --text-dark: #4a3a3e;
    --band-tint: rgba(255, 255, 255, 0.35);
  }
  * { box-sizing: border-box; margin: 0; padding: 0; }
  html, body {
    width: 1200px;
    height: 900px;
    overflow: hidden;
    background: var(--backdrop);
  }
  .canvas {
    position: relative;
    width: 1200px;
    height: 900px;
  }
  .card {
    position: absolute;
    top: 110px;
    width: 380px;
    height: 680px;
    border-radius: 16px;
    overflow: hidden;
    background:
      radial-gradient(ellipse 70% 40% at 30% 38%, var(--card-pink-light) 0%, transparent 70%),
      radial-gradient(ellipse 80% 30% at 70% 62%, rgba(255,255,255,0.45) 0%, transparent 70%),
      radial-gradient(ellipse 60% 50% at 90% 10%, var(--card-pink-deep) 0%, transparent 70%),
      var(--card-pink);
  }
  .card--front { left: 170px; }
  .card--back { left: 650px; }

  .card__swirl {
    position: absolute;
    inset: 0;
    width: 100%;
    height: 100%;
  }

  .brand {
    display: flex;
    align-items: center;
    gap: 12px;
    font-family: "Comfortaa", sans-serif;
    font-weight: 700;
    color: var(--brand-crimson);
    white-space: nowrap;
  }
  .brand__mark {
    width: 30px;
    height: 30px;
    border-radius: 6px;
    background: var(--brand-crimson);
    flex: none;
  }
  .card--front .brand {
    position: absolute;
    top: 318px;
    left: 0;
    right: 0;
    justify-content: center;
    font-size: 36px;
  }
  .card--back .brand {
    position: absolute;
    bottom: 38px;
    left: 0;
    right: 0;
    justify-content: center;
    font-size: 34px;
  }

  .contact-band {
    position: absolute;
    top: 198px;
    left: 0;
    right: 0;
    height: 52px;
    background: var(--band-tint);
  }
  .holder-name {
    position: absolute;
    top: 204px;
    left: 24px;
    font-family: "Delius", cursive;
    font-size: 30px;
    color: var(--brand-crimson);
    letter-spacing: 0.5px;
  }
  .contact-list {
    position: absolute;
    top: 272px;
    left: 34px;
    list-style: none;
    font-family: "Comfortaa", sans-serif;
    font-size: 12px;
    color: var(--text-dark);
    line-height: 20px;
  }
  .contact-list li {
    display: flex;
    align-items: center;
    gap: 8px;
  }
  .contact-list svg { width: 12px; height: 12px; flex: none; }
  .contact-list .contact-web { margin-top: 10px; }
  .contact-abn {
    position: absolute;
    top: 372px;
    left: 70px;
    font-family: "Comfortaa", sans-serif;
    font-size: 12px;
    color: var(--text-dark);
  }
</style>
</head>
<body>
<main class="canvas">

  <section class="card card--front" aria-label="Card front">
    <svg class="card__swirl" viewBox="0 0 380 680" aria-hidden="true">
      <path d="M-20 250 C 100 170, 260 180, 400 120" fill="none" stroke="#ffffff" stroke-opacity="0.35" stroke-width="2"/>
      <path d="M-20 470 C 120 400, 260 430, 400 380" fill="none" stroke="#ffffff" stroke-opacity="0.3" stroke-width="2"/>
      <path d="M60 680 C 140 560, 250 520, 400 500" fill="none" stroke="#e79fae" stroke-opacity="0.35" stroke-width="2"/>
    </svg>
    <div class="brand">
      <span class="brand__mark"></span>
      <span class="brand__name">Lomevu Linkup</span>
    </div>
  </section>

  <section class="card card--back" aria-label="Card back">
    <svg class="card__swirl" viewBox="0 0 380 680" aria-hidden="true">
      <path d="M-20 150 C 120 80, 260 110, 400 60" fill="none" stroke="#ffffff" stroke-opacity="0.35" stroke-width="2"/>
      <path d="M-20 520 C 120 460, 250 480, 400 430" fill="none" stroke="#ffffff" stroke-opacity="0.3" stroke-width="2"/>
    </svg>

    <div class="contact-band"></div>
    <h1 class="holder-name">Tobin Wexmoor</h1>

    <ul class="contact-list">
      <li>
        <svg viewBox="0 0 12 12" aria-hidden="true"><rect x="1" y="4" width="10" height="7" rx="1.5" fill="#c61f3f"/><path d="M1 4 Q6 0 11 4" fill="none" stroke="#c61f3f" stroke-width="1.6"/><circle cx="6" cy="7.5" r="1.6" fill="#f8c8d1"/></svg>
        <span>+468213579 (Singapore)</span>
      </li>
      <li>
        <svg viewBox="0 0 12 12" aria-hidden="true"><rect x="1" y="4" width="10" height="7" rx="1.5" fill="#c61f3f"/><path d="M1 4 Q6 0 11 4" fill="none" stroke="#c61f3f" stroke-width="1.6"/><circle cx="6" cy="7.5" r="1.6" fill="#f8c8d1"/></svg>
        <span>+315792846 (Australia)</span>
      </li>
      <li>
        <svg viewBox="0 0 12 12" aria-hidden="true"><rect x="1" y="4" width="10" height="7" rx="1.5" fill="#c61f3f"/><path d="M1 4 Q6 0 11 4" fill="none" stroke="#c61f3f" stroke-width="1.6"/><circle cx="6" cy="7.5" r="1.6" fill="#f8c8d1"/></svg>
        <span>+729384615 (America)</span>
      </li>
      <li class="contact-web">
        <svg viewBox="0 0 12 12" aria-hidden="true"><circle cx="6" cy="6" r="5" fill="none" stroke="#c61f3f" stroke-width="1.2"/><ellipse cx="6" cy="6" rx="2.2" ry="5" fill="none" stroke="#c61f3f" stroke-width="1"/><line x1="1" y1="6" x2="11" y2="6" stroke="#c61f3f" stroke-width="1"/></svg>
        <span>www.lomevu-linkup.example</span>
      </li>
    </ul>
    <p class="contact-abn">ABN 86420913</p>

    <div class="brand">
      <span class="brand__mark"></span>
      <span class="brand__name">Lomevu Linkup</span>
    </div>
  </section>

</main>
</body>
</html>
```